TRIVEX-PRO Web Design

We are a Health, Safety, Environmental & Quality Recruitment Agency, our clients are major corporate Mining, Oil & Gas and Engineering companies. We have offices in Perth & Melbourne, Australia

The website should be very functional & easy to navigate

BUT REALLY LOOKING FOR WOW FACTOR!
Updates

Please Note: TRIVEX HOLDINGS IS OUR OLD COMPANY THE NEW ONE IS "TRIVEX-PRO" 

Some idea's from our competitors:

http://www.guardlinemerit.com.au/
http://www.wardenplacement.com.au/
http://www.keelhunt.com.au/
http://www.brqstaffing.co.uk/
http://www.laborvane.com/health-safety-environment-jobs

Would love to see some of our valued clients and there logos

still looking for wow factor

Industry/Entity Type

Mining

Requirements
Must have
• A place where candidates can upload there resumes & other contact details
• eg: http://www.guardlinemerit.com.au/candidates/register-your-resume/
• A place we can load jobs on to eg: http://www.guardlinemerit.com.au/vacancies/
• Contact details:
• Perth: 17 Brindlecombe Ave, West Perth, Western Australia 6005
• t: 08 9517 3064 | f: 08 9517 3070 |
• Melbourne: Level 1, 212 Harrowgate Street, Melbourne, Victoria 3000
• t: 03 9655 4217| f: 03 9655 4290 |
• e: dmorl@trivexpro.com.au | w: http://www.trivexpro.com.au

```html
<!DOCTYPE html>
<html lang="en">
<head>
<meta charset="utf-8">
<title>trivexpro – HSEQ Recruitment</title>
<link rel="stylesheet" href="https://fonts.googleapis.com/css2?family=PT+Sans:ital,wght@0,400;0,700;1,400;1,700&family=Rokkitt:wght@400;500&display=swap">
<style>
:root{
  --blue:#1a8ac4;
  --blue-dark:#0f6ea3;
  --ink:#333;
  --text:#555;
  --bg:#ebebeb;
  --nav:#1d1d1d;
  --footer:#333;
  --btn:#454545;
}
*{margin:0;padding:0;box-sizing:border-box}
html,body{width:893px;height:1200px;overflow:hidden}
body{position:relative;background:var(--bg);font-family:"PT Sans",sans-serif;color:var(--text)}
.abs{position:absolute}
.serif{font-family:"Rokkitt",serif}

.brand{left:97px;top:6px;display:flex;align-items:center;gap:10px}
.brand-mark{width:98px;height:98px;background:linear-gradient(135deg,#9aa3aa,#1fa3dc 55%,#5a636b)}
.brand-name{font-size:44px;font-weight:400;color:#555;letter-spacing:1px}
.phone{left:612px;top:8px;display:flex;align-items:center;gap:6px;font-size:19px;color:#333}
.connected{left:718px;top:53px;font-size:11px;font-weight:700;font-style:italic;color:var(--blue)}
.social{top:72px;width:28px;height:28px;border-radius:50%;background:var(--blue-dark);color:#fff;font-size:6px;display:flex;align-items:center;justify-content:center}

.nav{left:0;top:110px;width:893px;height:48px;background:var(--nav)}
.nav a{position:absolute;top:0;height:48px;line-height:48px;color:#fff;text-decoration:none;font-size:13px}
.nav a.active{background:var(--blue);width:50px;text-align:center}
.nav a.active::before{content:"";position:absolute;left:20px;top:0;border:5px solid transparent;border-top-color:#111}
.search{left:612px;top:12px;width:192px;height:25px;border:1px solid #333;background:#161616;color:#aaa;font-size:9px;line-height:23px;padding-left:15px}
.search-btn{right:0;top:0;width:32px;height:23px;background:#252525}
.nav-sep{left:604px;top:8px;width:1px;height:32px;background:#333}

.hero{left:0;top:160px;width:893px;height:444px;
  background:
    radial-gradient(ellipse 260px 160px at 230px 340px,rgba(255,214,90,.95),rgba(240,150,40,.6) 45%,rgba(200,100,20,0) 100%),
    radial-gradient(ellipse 200px 260px at 40px 250px,rgba(230,150,40,.75),rgba(230,150,40,0) 100%),
    radial-gradient(ellipse 220px 200px at 820px 380px,rgba(210,120,40,.6),rgba(210,120,40,0) 100%),
    linear-gradient(180deg,#27406b 0%,#3f6296 28%,#6f85a8 50%,#9a8b86 66%,#c47a34 82%,#7b3d12 100%)}

.panel{left:87px;top:514px;width:719px;height:437px;background:#fff;box-shadow:0 0 6px rgba(0,0,0,.15)}
.title{font-size:25px;color:var(--ink);text-align:center;font-weight:400}
.title span{color:var(--blue)}
.welcome{left:0;top:10px;width:719px}
.dots{left:12px;top:49px;width:695px;border-top:1px dotted #bbb}
.intro{left:12px;top:55px;width:694px;font-size:9.8px;line-height:15.6px;text-align:justify;color:var(--text)}
.register{left:247px;top:163px;width:206px;height:34px;border-radius:4px;background:linear-gradient(#2aa1db,#0d73ad);box-shadow:0 0 0 2px #d7e9f3;color:#fff;font-size:23px;text-align:center;line-height:34px}
.rule{left:8px;top:215px;width:703px;border-top:1px solid #ddd}
.col-title{top:233px;font-size:16px;color:var(--blue);display:flex;align-items:center;gap:6px;font-weight:400}
.col-title i{display:block;width:83px;height:3px;background:#ddd}
.frame{top:262px;width:165px;height:78px;border:1px solid #ddd;padding:3px;box-shadow:0 0 3px rgba(0,0,0,.1)}
.frame div{width:100%;height:100%}
.col-text{top:346px;width:168px;font-size:9.8px;line-height:14.5px;text-align:justify}
.btn{top:399px;width:70px;height:17px;background:var(--btn);color:#fff;font-size:8.5px;text-align:center;line-height:17px}

.clients{left:0;top:958px;width:893px}
.client-rule{left:96px;top:990px;width:701px;border-top:1px solid #ddd}
.client{top:1009px;font-size:10px;font-weight:700;display:flex;align-items:center;gap:4px}
.client b{display:block;width:10px;height:10px}

.footer{left:0;top:1052px;width:893px;height:148px;background:var(--footer);color:#ddd}
.office{top:9px}
.office h3{font-family:"Rokkitt",serif;font-weight:400;font-size:16px;color:#fff;margin-bottom:8px}
.office p{font-size:8.6px;font-style:italic;line-height:15.7px}
.vsep{top:6px;width:1px;height:104px;background:#4a4a4a}
.foot-rule{left:96px;top:118px;width:701px;border-top:1px solid #444}
.copy{left:0;top:124px;width:893px;display:flex;justify-content:center;align-items:center;gap:6px;font-size:8.6px}
.copy b{display:block;width:18px;height:18px;background:#888}
</style>
</head>
<body>

<header>
  <div class="abs brand"><div class="brand-mark"></div><div class="brand-name">trivexpro</div></div>
  <div class="abs phone">
    <svg width="34" height="34" viewBox="0 0 34 34"><circle cx="17" cy="17" r="15" fill="none" stroke="#777" stroke-width="2"/><path d="M13 9c-3 3-3 12 4 17l3-3-3-3-2 1c-1-2-1-5 0-7l2 1 2-3z" fill="var(--blue)"/></svg>
    <span>+61 (08) 9471 2058</span>
  </div>
  <div class="abs connected">Get Connected:</div>
  <div class="abs social" style="left:696px">Nookly</div>
  <div class="abs social" style="left:733px">Chirpo</div>
  <div class="abs social" style="left:770px">Proflink</div>
</header>

<nav class="abs nav">
  <a class="active" href="#" style="left:81px">Home</a>
  <a href="#" style="left:143px">Job Seekers</a>
  <a href="#" style="left:235px">Employers</a>
  <a href="#" style="left:319px">Vacancies</a>
  <a href="#" style="left:400px">About Us</a>
  <a href="#" style="left:479px">News</a>
  <a href="#" style="left:537px">Contact</a>
  <div class="abs nav-sep"></div>
  <div class="abs search">Search Keyword
    <div class="abs search-btn"><svg width="32" height="23" viewBox="0 0 32 23"><circle cx="15" cy="10" r="5" fill="#3ba9e0" stroke="#9bd3f0" stroke-width="1.5"/><path d="M19 14l4 4" stroke="#9bd3f0" stroke-width="2"/></svg></div>
  </div>
</nav>

<div class="abs hero" role="img" aria-label="Industrial processing plant at dusk with glowing lights and tall chimney stacks"></div>

<main class="abs panel">
  <h1 class="abs title serif welcome">Welcome <span>Message</span></h1>
  <div class="abs dots"></div>
  <p class="abs intro"><b><i>Aenean aliquet erat ipsum, nec ornare ante tempor rutrum. Morbi vitae erat lobortis, tincidunt velit et, consectetur quam.</i></b> Praesent vel lacus cursus, congue diam varius, dignissim elit. Integer luctus urna at metus volutpat eleifend. Etiam tellus urna, fringilla in turpis sed, ullamcorper pretium augue. Nullam a adipiscing nisi. Donec sodales mi in felis lobortis, et feugiat lacus sagittis. Aliquam faucibus, mi eget hendrerit lobortis, urna quam malesuada risus, sit amet bibendum quam mauris vitae nunc.<br>Ut leo felis, euismod non vulputate in, rhoncus posuere ante. Maecenas nec odio vitae nisi volutpat hendrerit at eget mauris. Nunc iaculis lectus nec lectus condimentum viverra. Aliquam erat volutpat. Mauris ultricies feugiat augue, in ullamcorper leo. Integer ornare sem non lectus molestie iaculis nec at ante.</p>
  <div class="abs register serif">Register Now</div>
  <div class="abs rule"></div>

  <h2 class="abs col-title serif" style="left:13px">Job Seekers<i></i></h2>
  <div class="abs frame" style="left:16px"><div role="img" aria-label="Two site workers in hard hats and safety vests" style="background:linear-gradient(180deg,#c8d3de,#6f8fb3 60%,#2f4d78)"></div></div>
  <p class="abs col-text" style="left:15px">Lorem ipsum dolor sit amet, consectetur adipiscing elit. Praesent suscipit risus ac velit ornare lobortis...</p>
  <div class="abs btn" style="left:111px">Register Now...</div>

  <h2 class="abs col-title serif" style="left:264px">Employers<i></i></h2>
  <div class="abs frame" style="left:264px"><div role="img" aria-label="Engineer on a phone in front of a refinery" style="background:linear-gradient(180deg,#6a95c9,#9fb4c8 55%,#4c5a6a)"></div></div>
  <p class="abs col-text" style="left:266px">Lorem ipsum dolor sit amet, consectetur adipiscing elit. Praesent suscipit risus ac velit ornare lobortis...</p>
  <div class="abs btn" style="left:362px">Click here...</div>

  <h2 class="abs col-title serif" style="left:512px">Vacancies<i></i></h2>
  <div class="abs frame" style="left:512px"><div role="img" aria-label="Stack of worn safety helmets" style="background:linear-gradient(135deg,#3a2a18,#b08a4e 50%,#5a4126)"></div></div>
  <p class="abs col-text" style="left:512px">Lorem ipsum dolor sit amet, consectetur adipiscing elit. Praesent suscipit risus ac velit ornare lobortis...</p>
  <div class="abs btn" style="left:611px">Click here...</div>
</main>

<section>
  <h2 class="abs title serif clients">Successful <span>Clients</span></h2>
  <div class="abs client-rule"></div>
  <div class="abs client" style="left:114px;color:#c9302c"><b style="background:#c9302c"></b>Corvane</div>
  <div class="abs client" style="left:206px;color:#1a8ac4"><b style="background:#1a8ac4"></b>Tallis Works</div>
  <div class="abs client" style="left:316px;color:#c9302c"><b style="border-radius:50%;border:1px solid #333"></b>Ninefold Ridge</div>
  <div class="abs client" style="left:417px;color:#e0352b"><b style="background:#e0352b"></b>Bramwell Studio</div>
  <div class="abs client" style="left:540px;color:#222"><b style="background:#222"></b>Ostra Co</div>
  <div class="abs client" style="left:623px;color:#222"><b style="background:#222;border-radius:50%"></b>Velmont Group</div>
  <div class="abs client" style="left:742px;color:#333"><b style="background:#333;border-radius:50%"></b>Pellar</div>
</section>

<footer class="abs footer">
  <div class="abs office" style="left:87px"><h3>Perth Office</h3><p>Suite 4, 96 Carrow Street Subiaco<br>Western Australia 6008<br>Phone: +61 (08) 9471 2058<br>Email: perth@trivexpro.com.au</p></div>
  <div class="abs vsep" style="left:244px"></div>
  <div class="abs office" style="left:260px"><h3>Brisbane Office</h3><p>Level 12, Marlow Plaza Two<br>118 Fenwick Street,<br>Brisbane Queensland 4000<br>Phone: +61 (07) 3284 6610<br>Email: brisbane@trivexpro.com.au</p></div>
  <div class="abs vsep" style="left:426px"></div>
  <div class="abs office" style="left:442px"><h3>Hong Kong Office</h3><p>22/F Linden Tower 9 Quarry Road<br>Wanchai, Hong Kong<br>Phone: +852 8046 3371<br>Email: hongkong@trivexpro.asia</p></div>
  <div class="abs vsep" style="left:634px"></div>
  <div class="abs office" style="left:649px"><h3>Seoul Office</h3><p>Level 18, Hanbit Tower 204<br>Seolleung-ro Samsung dong,<br>Gangnam-Gu Seoul, Republic of Korea<br>Phone: +82 (0) 2 5318 7402<br>Email: seoul@trivex.com.asia</p></div>
  <div class="abs foot-rule"></div>
  <div class="abs copy"><b></b><span>trivexpro, copy right © 2013, Terms &amp; Conditions | Privacy Policy</span></div>
</footer>

</body>
</html>
```